Real Estate Sign

My company is in need of a redesign for our real estate lawn sign. The sign should show our logo, the phrase "For Sale", our phone number 314-587-2049 and website www.HomvexTX.com.
Updates

Hello

Thank you for your submissions.  I am looking for the website and phone number to be very visible from a good distance.  I do also want to stay within the colors of my logo. Too many colors could be expensive to reproduce.

Thank you
Trevor

I favor clean, straight lines and design.  I prefer not to add any other graphics or logos on the sign.  The logo and name are enough. I am looking for readability from a good distance and prefer calls to action like call 314-592-2049 for information or visit www.HomvexTX.com to schedule tour today!  I don't really need FOR SALE to be so prominent.

thanks for all the submissions.
Trevor

Trevor

Industry/Entity Type

Real Estate

```html
<!DOCTYPE html>
<html lang="en">
<head>
<meta charset="utf-8">
<title>Homvex Realty – Lawn Sign</title>
<link rel="stylesheet" href="https://fonts.googleapis.com/css2?family=Source+Sans+3:wght@400;600&display=swap">
<style>
  :root {
    --canvas: #ffffff;
    --navy: #0b4f86;
    --panel-top: #0c4f88;
    --panel-mid: #1763a6;
    --panel-low: #11579a;
    --sky: #41a9e0;
    --white: #ffffff;
  }
  * { margin: 0; padding: 0; box-sizing: border-box; }
  html, body {
    width: 1200px; height: 1000px; overflow: hidden;
    background: var(--canvas);
    font-family: "Source Sans 3", "PT Sans", sans-serif;
  }
  .canvas { position: relative; width: 1200px; height: 1000px; }
  .sign {
    position: absolute; left: 315px; top: 84px;
    width: 570px; height: 769px;
    background: var(--navy);
  }
  .sign-frame {
    position: absolute; left: 13px; top: 11px;
    width: 545px; height: 747px;
    border: 3px solid var(--white);
  }
  .sign-field {
    position: absolute; left: 16px; top: 14px;
    width: 539px; height: 608px;
    background: radial-gradient(ellipse at 70% 45%, var(--panel-mid) 0%, var(--panel-low) 55%, var(--panel-top) 100%);
  }
  .sign-band {
    position: absolute; left: 16px; top: 622px;
    width: 539px; height: 132px;
    background: var(--sky);
    display: flex; align-items: center; justify-content: center;
  }
  .band-label {
    color: var(--white); font-weight: 400;
    font-size: 92px; line-height: 1; letter-spacing: 1px;
  }
  .line {
    position: absolute; left: 0; width: 570px;
    text-align: center; color: var(--white); font-weight: 400;
    white-space: nowrap; line-height: 1;
  }
  .brand-name { top: 130px; font-size: 66px; font-weight: 600; }
  .cta-lead { top: 258px; font-size: 44px; }
  .cta-visit { top: 322px; font-size: 44px; }
  .cta-web { top: 384px; font-size: 49px; }
  .cta-or { top: 455px; font-size: 43px; }
  .cta-phone { top: 522px; font-size: 64px; }
</style>
</head>
<body>
<main class="canvas">
  <section class="sign">
    <div class="sign-frame"></div>
    <div class="sign-field" role="img" aria-label="Soft blue background with fine sweeping line texture"></div>
    <div class="line brand-name">Homvex Realty</div>
    <p class="line cta-lead">To Schedule a Tour</p>
    <p class="line cta-visit">Visit</p>
    <p class="line cta-web">www.HomvexTX.com</p>
    <p class="line cta-or">or call</p>
    <p class="line cta-phone">314-587-2049</p>
    <div class="sign-band"><span class="band-label">FOR SALE</span></div>
  </section>
</main>
</body>
</html>
```